Flyer-Design für Initiative für bunte Freizeitkultur
Zielgruppe
Initiative für bunte Freizeitkultur. Wir haben im Januar diesen Jahres einen neuen Jugendtreff eröffnet und benötigen dafür einen Flyer der möglichst ansprechend für Jugendliche zwischen 10 und 18 Jahren ist. Der Flyer sollte beidseitig sein und die beschriebenen Vorgaben enthalten.
Aufgabenstellung
Größe A5.
Folgende Informationen müssen enthalten sein:
Vorderseite:
Name des Jugendtreffs: Jugendtreff Korvane
Träger: Initiative für bunte Freizeitkultur e.V.
Angebote: GX7 / Billard / Tischtennis / Free-Wlan / Fitness / Essen und Getränke / Werkstatt / Chillen / Räume selbst gestalten
'follow us on Fotello' inklusive fotello Logo.

```html
<!DOCTYPE html>
<html lang="de">
<head>
<meta charset="utf-8">
<title>Jugendtreff Korvane – Flyer A5</title>
<link rel="stylesheet" href="https://fonts.googleapis.com/css2?family=Permanent+Marker&family=Encode+Sans+Condensed:wght@400;600&display=swap">
<style>
  :root {
    --stage: #e9e6e2;
    --orange: #f2771c;
    --deep-orange: #e2461a;
    --red: #c8241b;
    --yellow: #f4d21f;
    --sky: #3fb2e6;
    --navy: #233a8f;
    --ink: #111111;
    --white: #ffffff;
    --marker: "Permanent Marker", cursive;
    --sans: "Encode Sans Condensed", sans-serif;
  }
  * { box-sizing: border-box; margin: 0; padding: 0; }
  html, body { width: 1200px; height: 982px; overflow: hidden; background: var(--stage); }
  .sheet {
    width: 1200px; height: 982px;
    display: flex; justify-content: center; align-items: center; gap: 28px;
  }
  .flyer {
    position: relative; width: 560px; height: 792px; overflow: hidden;
    box-shadow: 0 6px 20px rgba(0,0,0,.18);
  }
  .marble {
    position: absolute; inset: 0;
    background:
      radial-gradient(circle at 30% 18%, var(--yellow) 0, transparent 28%),
      radial-gradient(circle at 78% 46%, var(--sky) 0, transparent 30%),
      radial-gradient(circle at 20% 70%, var(--red) 0, transparent 30%),
      radial-gradient(circle at 62% 88%, var(--orange) 0, transparent 34%),
      linear-gradient(160deg, var(--deep-orange), var(--orange) 40%, var(--navy) 60%, var(--orange));
  }
  .marble--back {
    background:
      radial-gradient(circle at 70% 30%, var(--sky) 0, transparent 32%),
      radial-gradient(circle at 25% 62%, var(--red) 0, transparent 30%),
      radial-gradient(circle at 75% 80%, var(--deep-orange) 0, transparent 30%),
      linear-gradient(200deg, var(--orange), var(--navy) 45%, var(--sky) 60%, var(--orange));
  }
  .silhouette {
    position: absolute;
    background: linear-gradient(180deg, #1a1a1a, var(--ink));
    border-radius: 40px 40px 6px 6px;
  }
  .front .silhouette { right: 40px; bottom: 40px; width: 150px; height: 420px; }
  .back .silhouette { right: 60px; top: 0; width: 120px; height: 190px; border-radius: 0 0 30px 30px; }

  .brand {
    position: absolute; top: 36px; left: 40px; right: 40px;
    display: flex; align-items: center; gap: 14px;
  }
  .brand__dot { width: 86px; height: 86px; border-radius: 50%; background: var(--orange); flex: none; }
  .brand__text { font-family: var(--sans); color: var(--white); }
  .brand__name { font-size: 34px; font-weight: 600; line-height: 1.05; }
  .brand__carrier { font-size: 17px; font-weight: 400; }

  .offers {
    position: absolute; left: 36px; top: 300px; width: 330px;
    font-family: var(--marker); color: var(--white); text-transform: uppercase;
    text-shadow: 2px 2px 0 var(--ink), -1px -1px 0 var(--ink), 1px -1px 0 var(--ink), -1px 1px 0 var(--ink);
  }
  .offers__row { font-size: 30px; line-height: 1.2; }
  .offers__title { font-size: 44px; line-height: 1.05; color: var(--yellow); margin: 10px 0; }

  .follow {
    position: absolute; top: 220px; left: 40px;
    display: flex; align-items: center; gap: 12px; color: var(--white);
  }
  .follow__square { width: 38px; height: 38px; border-radius: 9px; background: var(--white); }
  .follow__handle { font-family: var(--marker); font-size: 26px; color: var(--yellow); text-transform: uppercase;
    text-shadow: 1px 1px 0 var(--ink); }
  .follow__hint { font-family: var(--sans); font-size: 15px; }

  .contact {
    position: absolute; right: 40px; bottom: 130px; text-align: right;
    font-family: var(--sans); color: var(--white); font-size: 20px; line-height: 1.35;
  }
  .contact__name { font-size: 26px; font-weight: 600; }
  .hours {
    position: absolute; left: 40px; right: 40px; bottom: 44px;
    font-family: var(--sans); color: var(--white); font-size: 26px; font-weight: 600;
  }
</style>
</head>
<body>
<main class="sheet">
  <section class="flyer front" aria-label="Vorderseite">
    <div class="marble" role="img" aria-label="Bunter Marmor-Hintergrund in Orange, Rot, Gelb und Blau"></div>
    <div class="silhouette" role="img" aria-label="Schwarze Silhouette einer stehenden Person mit Spraydose"></div>
    <header class="brand">
      <span class="brand__dot"></span>
      <div class="brand__text">
        <p class="brand__name">Jugendtreff Korvane</p>
        <p class="brand__carrier">Initiative für bunte Freizeitkultur e.V.</p>
      </div>
    </header>
    <div class="offers">
      <p class="offers__row">Billard · Räume</p>
      <p class="offers__row">Fitness · selbst</p>
      <p class="offers__row">gestalten</p>
      <p class="offers__title">Jugendtreff<br>Korvane</p>
      <p class="offers__row">Essen &amp;</p>
      <p class="offers__row">Getränke · Free WLAN</p>
      <p class="offers__row">Werkstatt</p>
      <p class="offers__row">GX7 · Chillen</p>
    </div>
  </section>

  <section class="flyer back" aria-label="Rückseite">
    <div class="marble marble--back" role="img" aria-label="Bunter Marmor-Hintergrund in Blau, Rot und Orange"></div>
    <div class="silhouette" role="img" aria-label="Schwarze Silhouette einer Person, oberer Ausschnitt"></div>
    <div class="follow">
      <span class="follow__square"></span>
      <div>
        <p class="follow__handle">jugendtreff_korvane</p>
        <p class="follow__hint">Follow us on Fotello</p>
      </div>
    </div>
    <address class="contact">
      <p class="contact__name">Jugendtreff Korvane</p>
      <p>Initiative für bunte Freizeitkultur e.V.</p>
      <p>Lindenbogen 12</p>
      <p>08451 Rabenhain</p>
      <p>03700/ 555 0142</p>
      <p>kontakt@jt-korvane.de</p>
    </address>
    <p class="hours">Öffnungszeiten: Di – Fr 14:00 Uhr bis 18:30 Uhr</p>
  </section>
</main>
</body>
</html>
```